Business card for our large format printing and installation business

We want a professional looking business card for our business. We manufacture and install Signs.

On the back of the card add this info
Large Format Graphics Printing & Installations, Event Graphics, Banners, Posters, Vehicle Fleet Graphics, Boat Wraps, Wall Murals, Decals,Displays,Signs,Plaques,Digital Signs

On the Front of the card add the Tallowfern Signs logo, plus On the back of the card add the Orange Tallowfern Wraps logo. The 2 vector logos are attached to the design brief.

Target Market(s)

Local business owners

Contact Information for Business Card

Colors
f37122
f68d4e
f9ba93

Requirements
Must have
• On the Front of the card add the Tallowfern Signs logo, plus On the back of the card add the Orange Tallowfern Wraps logo. The 2 vector logos are attached to the design brief.

```html
<!DOCTYPE html>
<html lang="en">
<head>
<meta charset="utf-8">
<title>Tallowfern Signs – Business Card</title>
<link rel="stylesheet" href="https://fonts.googleapis.com/css2?family=Open+Sans:wght@800&family=Tinos&display=swap">
<style>
  :root {
    --backdrop: #8c8c8c;
    --card: #2a2728;
    --edge: #f37122;
    --gold: #f7a41c;
    --band-start: #f6921e;
    --band-mid: #ffe600;
    --band-end: #f39a1e;
    --ink-dark: #1e1b1c;
    --text-light: #f2f2f2;
  }
  * { box-sizing: border-box; margin: 0; padding: 0; }
  html, body { width: 1200px; height: 960px; overflow: hidden; }
  body {
    background: var(--backdrop);
    display: flex;
    flex-direction: column;
    align-items: center;
    justify-content: center;
    gap: 50px;
  }
  .card {
    position: relative;
    width: 700px;
    height: 400px;
    background: var(--card);
    border-bottom: 4px solid var(--edge);
    box-shadow: 0 10px 24px rgba(0,0,0,0.35);
    overflow: hidden;
  }
  .brand-name {
    font-family: "Open Sans", sans-serif;
    font-weight: 800;
    color: var(--gold);
    letter-spacing: -0.5px;
    line-height: 1;
    white-space: nowrap;
  }
  .card-front .brand-name {
    position: absolute;
    left: 50%;
    top: 50%;
    transform: translate(-50%, -50%);
    font-size: 60px;
  }
  .card-back .brand-name {
    position: absolute;
    right: 40px;
    top: 92px;
    font-size: 44px;
  }
  .name-band {
    position: absolute;
    left: 0;
    top: 146px;
    width: 410px;
    height: 58px;
    background: linear-gradient(90deg, var(--band-start) 0%, var(--band-mid) 55%, var(--band-end) 100%);
    padding: 7px 0 0 150px;
    font-family: "Open Sans", sans-serif;
    font-weight: 800;
    color: var(--ink-dark);
  }
  .person-name { font-size: 22px; line-height: 1.1; }
  .person-role { font-size: 16px; line-height: 1.2; padding-left: 18px; }
  .contact {
    position: absolute;
    left: 200px;
    top: 226px;
    font-family: "Tinos", serif;
    font-size: 16px;
    color: var(--text-light);
    line-height: 1.25;
  }
  .address { margin-bottom: 8px; }
  .address span { display: block; }
  .address span + span { padding-left: 14px; }
  .contact-list { list-style: none; padding-left: 28px; }
  .contact-list li { display: flex; align-items: center; gap: 8px; }
  .contact-list svg { width: 13px; height: 13px; fill: var(--gold); flex: none; }
</style>
</head>
<body>

<section class="card card-front" aria-label="Card front">
  <div class="brand-name">Tallowfern Signs</div>
</section>

<section class="card card-back" aria-label="Card back">
  <div class="brand-name">Tallowfern Signs</div>
  <div class="name-band">
    <div class="person-name">Daniel Harrow</div>
    <div class="person-role">President</div>
  </div>
  <div class="contact">
    <p class="address">
      <span>2140 Birchwood Court</span>
      <span>Anchorage, Alaska 34512</span>
    </p>
    <ul class="contact-list">
      <li><svg viewBox="0 0 16 16"><path d="M3 1l3 3-2 2c1 2 4 5 6 6l2-2 3 3-2 2C7 15 1 9 1 3z"/></svg>555-214-0186</li>
      <li><svg viewBox="0 0 16 16"><path d="M4 0h8v16H4zM5.5 2v10h5V2z"/></svg>555-317-4420</li>
      <li><svg viewBox="0 0 16 16"><path d="M4 1h8v4H4zM1 6h14v7h-3v2H4v-2H1zM5 10v4h6v-4z"/></svg>555-408-2273</li>
      <li><svg viewBox="0 0 16 16"><path d="M0 3h16v10H0zM1.5 4.5L8 9l6.5-4.5"/></svg>info@tallowfernsigns.com</li>
      <li><svg viewBox="0 0 16 16"><circle cx="8" cy="8" r="7"/></svg>www.tallowfernsigns.com</li>
    </ul>
  </div>
</section>

</body>
</html>
```